Modern, Sleek Business Card Design for Corvane Systems

Please create a modern business card, preferably all black with white logo and writing for Corvane Systems, a defense and aerospace company.

Contact Information for Business Card

symbol on one side and name, title, contact info on the other side.

```html
<!DOCTYPE html>
<html lang="en">
<head>
<meta charset="utf-8">
<title>Corvane Systems – Business Card</title>
<link href="https://fonts.googleapis.com/css2?family=Montserrat:wght@500;700&family=Arimo:wght@400&display=swap" rel="stylesheet">
<style>
  :root {
    --stage: #3b3b3d;
    --card: #1f1f20;
    --card-deep: #151516;
    --ink: #ffffff;
    --ink-soft: #e6e6e6;
    --pattern-light: #5a5a5c;
    --pattern-dark: #161617;
  }
  * { box-sizing: border-box; margin: 0; padding: 0; }
  html, body { width: 1200px; height: 915px; overflow: hidden; }
  body {
    background: var(--stage);
    display: flex;
    flex-direction: column;
    align-items: center;
    justify-content: center;
    gap: 60px;
  }
  .card {
    position: relative;
    width: 640px;
    height: 366px;
    border-radius: 22px;
    background: var(--card);
    overflow: hidden;
    box-shadow: 0 14px 30px rgba(0,0,0,0.35);
  }

  /* Back side */
  .card--back { background: var(--card-deep); }
  .back-pattern {
    position: absolute;
    inset: 0;
    background: linear-gradient(120deg, var(--pattern-light) 0%, #2a2a2c 35%, var(--pattern-dark) 70%);
  }
  .back-wordmark {
    position: absolute;
    right: 48px;
    top: 162px;
    font-family: "Montserrat", sans-serif;
    font-weight: 700;
    font-size: 18px;
    letter-spacing: 3px;
    color: var(--ink);
  }

  /* Front side */
  .wordmark {
    position: absolute;
    left: 46px;
    top: 58px;
    font-family: "Montserrat", sans-serif;
    font-weight: 500;
    font-size: 30px;
    letter-spacing: 6px;
    color: var(--ink);
    line-height: 1.15;
    width: 320px;
  }
  .identity {
    position: absolute;
    left: 46px;
    top: 160px;
    color: var(--ink);
  }
  .identity__name {
    font-family: "Montserrat", sans-serif;
    font-weight: 700;
    font-size: 22px;
    letter-spacing: 0.5px;
  }
  .identity__title {
    font-family: "Arimo", sans-serif;
    font-size: 15px;
    color: var(--ink-soft);
    margin-top: 2px;
  }
  .address {
    font-family: "Arimo", sans-serif;
    font-size: 15px;
    line-height: 1.3;
    color: var(--ink-soft);
    margin-top: 16px;
    margin-left: 46px;
  }
  .contact-list {
    list-style: none;
    margin-top: 14px;
    margin-left: 46px;
    font-family: "Arimo", sans-serif;
    font-size: 15px;
    color: var(--ink-soft);
  }
  .contact-list li {
    display: flex;
    align-items: center;
    gap: 9px;
    line-height: 1.55;
  }
  .contact-list svg { width: 13px; height: 13px; fill: var(--ink); flex: none; }
  .brand-block {
    position: absolute;
    right: 52px;
    top: 62px;
    width: 236px;
    height: 236px;
    background: var(--ink);
  }
</style>
</head>
<body>

  <section class="card card--back">
    <div class="back-pattern" role="img" aria-label="Repeating tonal brand pattern across the card back"></div>
    <div class="back-wordmark">CORVANE SYSTEMS</div>
  </section>

  <section class="card card--front">
    <div class="wordmark">CORVANE SYSTEMS</div>
    <div class="brand-block" aria-hidden="true"></div>

    <div class="identity">
      <div class="identity__name">DANIEL MARSH</div>
      <div class="identity__title">CEO/Founder</div>
    </div>

    <div style="position:absolute; left:0; top:212px;">
      <p class="address">P.O Box 4170 Harbor Street Name<br>Westfield AB 10234</p>
      <ul class="contact-list">
        <li>
          <svg viewBox="0 0 16 16"><path d="M3.6 1.2l2.3 2.8-1.3 1.6c.9 2 2.6 3.7 4.6 4.6l1.6-1.3 2.8 2.3-1.4 2.4C7 13.3 2.7 9 1.2 3z"/></svg>
          +52-55-3901-2264
        </li>
        <li>
          <svg viewBox="0 0 16 16"><path d="M1 3h14v10H1z M2.5 4.3v.3L8 8.6l5.5-4v-.3z" fill-rule="evenodd"/></svg>
          info@corvanesystems.com
        </li>
        <li>
          <svg viewBox="0 0 16 16"><path d="M8 1a7 7 0 100 14A7 7 0 008 1zm0 1.4c.8 0 1.7 1.6 2 4.1H6c.3-2.5 1.2-4.1 2-4.1zM2.5 7.5h2.2c0 .4 0 .8 0 1H2.5zm8.8 0h2.2v1h-2.2zM6 9.5h4c-.3 2.5-1.2 4.1-2 4.1s-1.7-1.6-2-4.1z"/></svg>
          www.corvanesystems.com
        </li>
      </ul>
    </div>
  </section>

</body>
</html>
```